Modern Innovative Business Card Design

We require a nice, modern, clean business card design, ready for upload to Cardomora. Our company develops online banking software solutions for small financial insitutions. The design should be clean, professional, but yet not "corporate boring". See www.fyrolt.com for an idea of business image and profile. The design should communicate innovation, be modern and fresh, yet look professional and established.

Target Market(s)

Finance industry, bankers, entrepreneurs

Industry/Entity Type

Financial

Contact Information for Business Card

Tobias Wendlerup
CEO

FYROLT BV
Lindenwerf 38
1027 HX Amsterdam
The Netherlands

Phone: +31 20 517 8036
Direct: +31 20 604 1758
Skype: tobias.fyrolt
ceo@fyrolt.com
www.fyrolt.com

Font styles to use
Sans Serif

Requirements
Must have
• Should look clean, modern and professional. File should be ready for upload to cardomora.
Should not have
• Boring standard corporate layout

```html
<!DOCTYPE html>
<html lang="en">
<head>
<meta charset="utf-8">
<title>FYROLT – Business Card</title>
<link rel="stylesheet" href="https://fonts.googleapis.com/css2?family=Open+Sans:wght@400;600;700&display=swap">
<style>
  :root {
    --green: #8cc63f;
    --ink: #4a4a4a;
    --ink-soft: #555555;
    --band-grey: #5a5a5a;
    --card: #ffffff;
    --backdrop: #e9e9e6;
    --rule: #6a6a6a;
  }
  * { box-sizing: border-box; margin: 0; padding: 0; }
  html, body {
    width: 1200px; height: 900px; overflow: hidden;
    background: var(--backdrop);
    font-family: "Open Sans", sans-serif;
  }
  .card {
    position: absolute; left: 120px; top: 170px;
    width: 960px; height: 560px;
    background: var(--card);
    border-radius: 30px;
    overflow: hidden;
    box-shadow: 0 10px 30px rgba(0,0,0,0.12);
    color: var(--ink);
  }
  .brand-name {
    position: absolute; left: 58px; top: 52px;
    font-size: 84px; font-weight: 600; letter-spacing: 4px;
    color: var(--ink-soft); line-height: 1;
  }
  .holder {
    position: absolute; right: 105px; top: 128px; text-align: right;
  }
  .holder-name {
    font-size: 30px; font-weight: 700; color: var(--green); line-height: 1.2;
  }
  .holder-title { font-size: 19px; color: var(--ink); margin-top: 2px; }
  .divider {
    position: absolute; left: 60px; right: 100px; top: 210px;
    height: 1.5px; background: var(--rule);
  }
  .contact-list {
    position: absolute; right: 66px; top: 232px;
    list-style: none; text-align: right;
  }
  .contact-list li {
    display: flex; justify-content: flex-end; align-items: center;
    gap: 14px; height: 31px;
    font-size: 21px; letter-spacing: 0.6px; color: var(--ink);
  }
  .contact-list svg { width: 22px; height: 22px; flex: none; }
  .address {
    position: absolute; left: 66px; top: 330px;
    font-size: 21px; line-height: 1.4; color: var(--ink);
  }
  .address .company { color: var(--green); font-weight: 700; }
  .band-green {
    position: absolute; left: 0; right: 0; bottom: 52px;
    height: 10px; background: var(--green);
  }
  .band-grey {
    position: absolute; left: 0; right: 0; bottom: 0;
    height: 52px; background: var(--band-grey);
  }
</style>
</head>
<body>
  <div class="card">
    <div class="brand-name">FYROLT</div>

    <div class="holder">
      <div class="holder-name">Tobias Wendlerup</div>
      <div class="holder-title">CEO</div>
    </div>

    <div class="divider"></div>

    <ul class="contact-list">
      <li>+31 20 517 8036
        <svg viewBox="0 0 24 24" aria-hidden="true"><path fill="#8cc63f" d="M6.6 10.8a15.2 15.2 0 0 0 6.6 6.6l2.2-2.2a1 1 0 0 1 1-.25 11.4 11.4 0 0 0 3.6.57 1 1 0 0 1 1 1V20a1 1 0 0 1-1 1A17 17 0 0 1 3 4a1 1 0 0 1 1-1h3.5a1 1 0 0 1 1 1c0 1.25.2 2.45.57 3.6a1 1 0 0 1-.25 1z"/></svg>
      </li>
      <li>+31 20 604 1758
        <svg viewBox="0 0 24 24" aria-hidden="true"><path fill="#8cc63f" d="M6.6 10.8a15.2 15.2 0 0 0 6.6 6.6l2.2-2.2a1 1 0 0 1 1-.25 11.4 11.4 0 0 0 3.6.57 1 1 0 0 1 1 1V20a1 1 0 0 1-1 1A17 17 0 0 1 3 4a1 1 0 0 1 1-1h3.5a1 1 0 0 1 1 1c0 1.25.2 2.45.57 3.6a1 1 0 0 1-.25 1z"/></svg>
      </li>
      <li>ceo@fyrolt.com
        <svg viewBox="0 0 24 24" aria-hidden="true"><rect x="2" y="5" width="20" height="14" rx="1.5" fill="#8cc63f"/><path d="M3 6l9 7 9-7" fill="none" stroke="#fff" stroke-width="1.6"/></svg>
      </li>
      <li>tobias.fyrolt
        <svg viewBox="0 0 24 24" aria-hidden="true"><circle cx="12" cy="12" r="10" fill="#8cc63f"/></svg>
      </li>
      <li>www.fyrolt.com
        <svg viewBox="0 0 24 24" aria-hidden="true"><circle cx="12" cy="12" r="9.5" fill="none" stroke="#8cc63f" stroke-width="2"/><ellipse cx="12" cy="12" rx="4" ry="9.5" fill="none" stroke="#8cc63f" stroke-width="1.6"/><path d="M2.5 12h19M4 7h16M4 17h16" stroke="#8cc63f" stroke-width="1.4"/></svg>
      </li>
    </ul>

    <div class="address">
      <div class="company">FYROLT BV</div>
      <div>Lindenwerf 38,</div>
      <div>1027 HX Amsterdam,</div>
      <div>The Netherlands</div>
    </div>

    <div class="band-green"></div>
    <div class="band-grey"></div>
  </div>
</body>
</html>
```